Need a powerful, eye-catching book cover design for a Public Relations book for Lawyers.

We need a beautiful, elegant, and professional cover for a public relations book. We’ll be selling this both to (1) creative, experienced legal marketers, and (2) conservative lawyers. It must grab their attention visually, and have a bold, easy to read headline. The cover image may wrap around to the back cover.SIZE: 6 x 9” 100 pagesTITLE: The Ultimate Public Relations Handbook for LawyersSUBHEAD: Make millions using media and the InternetCO-AUTHORSRoss Fishman, JDJohn HellermanInclude a CALLOUT quote: “The definitive PR book. Simple and powerful.” – Hal Brisket, SkaddenGRAPHICS:You may use one of the attached photos, crop or flip them however you’d like, or use something else entirely. DESCRIPTION for the back cover:Why do some law firms have the best reputations or command the highest hourly rates? Why are some the go-to firms or thought leaders in particular specialties? Why are your competitors in the media more than you? Two words: Public relations. The co-authors are known worldwide as leaders in public relations, legal marketing, and branding. Mark Tolliver is called, “A PR Guru.” Bar Ledger magazine wrote ““Many people consider Dale Warbeck to be the nation’s foremost expert on law firm marketing.”Hal Brisket built Valmont into the first firm to generate $1 billion in revenue. Nadine Cortez is the nation’s go-to lawyer for women’s issues. Your home town’s top PI lawyer gets the first look at the biggest cases. Why? Strategic, intentional, effective PR. Are you tired of toiling in anonymity? Want to earn the attention of reporters and editors who can build your credentials and reputation for expertise? Wouldn’t it be nice to have more clients begging you to represent them because they heard you were the best in town? That is what public relations is designed to do. Want to get more respect, earn more clients, and charge higher rates? Get known as a thought leader in a specialty practice or industry? Public relations could be your most-important marketing tool. And this book will teach you precisely how. Ready to catapult your practice to new heights? Take a deep breath and dive in….

Target Market(s)

1. Creative marketing professionals
2. Conservative 40-year-old lawyers

Industry/Entity Type

Legal

Font styles to use
Serif

Requirements
Must have
• Want a simple, bold, eye catching design conveying professionalism and quality. This is a practical, how-to book. We need a simple design and strong headline that will work well at a small thumbnail size on Quiverly.
Nice to have
• Perhaps the microphone could wrap around the cover? A tight crop of a microphone that creates an abstract could work. Let's create something memorable.

```html
<!DOCTYPE html>
<html lang="en">
<head>
<meta charset="utf-8">
<title>The Complete Press Outreach Guidebook for Attorneys — Book Cover</title>
<link rel="stylesheet" href="https://fonts.googleapis.com/css2?family=Montserrat:ital,wght@0,400;0,500;0,600;0,800;1,700&family=Varela+Round&display=swap">
<style>
  :root {
    --page-bg: #eef0f2;
    --cover-blue: #1d7db2;
    --cover-blue-deep: #17608c;
    --cover-blue-light: #2a8cc0;
    --title-white: #ffffff;
    --accent-yellow: #f3c53b;
    --mic-silver: #c9ced3;
    --mic-wood: #8a4d2c;
  }
  * { box-sizing: border-box; margin: 0; padding: 0; }
  html, body {
    width: 1200px; height: 999px; overflow: hidden;
    background: var(--page-bg);
  }
  .spread {
    position: relative; width: 1200px; height: 999px;
    display: flex; justify-content: center; align-items: center; gap: 40px;
  }
  .cover {
    position: relative; width: 540px; height: 810px;
    background: radial-gradient(ellipse at 50% 45%, var(--cover-blue-light) 0%, var(--cover-blue) 55%, var(--cover-blue-deep) 100%);
    color: var(--title-white);
    box-shadow: 0 4px 14px rgba(0,0,0,0.12);
  }

  /* Back cover */
  .back-copy {
    position: absolute; left: 42px; right: 40px; top: 90px;
    font-family: "Montserrat", sans-serif; font-weight: 400;
    font-size: 12.4px; line-height: 19px; letter-spacing: -0.25px;
    text-align: justify;
  }
  .back-copy p + p { margin-top: 18px; }
  .back-mic {
    position: absolute; left: 50%; top: 605px; width: 62px; height: 185px;
    transform: translateX(-50%);
  }

  /* Front cover */
  .title {
    position: absolute; left: 0; right: 0; top: 72px;
    text-align: center; font-family: "Montserrat", sans-serif;
    font-weight: 800; text-transform: uppercase; line-height: 1.04;
    letter-spacing: -0.5px;
  }
  .title .title-small { display: block; font-size: 29px; }
  .title .title-large { display: block; font-size: 45px; }
  .subtitle {
    position: absolute; left: 0; right: 0; top: 272px; text-align: center;
    font-family: "Varela Round", sans-serif; font-size: 19px;
    color: var(--accent-yellow);
  }
  .front-mic {
    position: absolute; left: 196px; top: 332px; width: 112px; height: 324px;
  }
  .callout {
    position: absolute; right: 34px; top: 500px; text-align: right;
    font-family: "Montserrat", sans-serif; font-style: italic; font-weight: 700;
    font-size: 14.5px; line-height: 1.35;
  }
  .callout cite { display: block; font-style: normal; font-weight: 600; }
  .credits {
    position: absolute; left: 0; right: 0; top: 712px; text-align: center;
    font-family: "Montserrat", sans-serif; color: var(--accent-yellow);
  }
  .credits .credits-label { font-weight: 800; font-size: 14px; letter-spacing: 0.3px; }
  .credits .author { font-weight: 500; font-size: 18px; line-height: 1.3; }
</style>
</head>
<body>
<main class="spread">
  <section class="cover back-cover">
    <div class="back-copy">
      <p>Why do some law firms have the best reputations or command the highest hourly rates? Why are some the go-to firms or thought leaders in particular specialties? Why are your competitors in the media more than you? Two words: Public relations.</p>
      <p>The co-authors are known worldwide as leaders in public relations, legal marketing, and branding. Mark Tolliver is called, “A PR Guru.” Bar Ledger magazine wrote ““Many people consider Dale Warbeck to be the nation’s foremost expert on law firm marketing.”Hal Brisket built Valmont into the first firm to generate $1 billion in revenue. Nadine Cortez is the nation’s go-to lawyer for women’s issues.</p>
      <p>Your home town’s top PI lawyer gets the first look at the biggest cases. Why? Strategic, intentional, effective PR. Are you tired of toiling in anonymity? Want to earn the attention of reporters and editors who can build your credentials and reputation for expertise? Wouldn’t it be nice to have more clients begging you to represent them because they heard you were the best in town? That is what public relations is designed to do.</p>
      <p>Want to get more respect, earn more clients, and charge higher rates? Get known as a thought leader in a specialty practice or industry? Public relations could be your most-important marketing tool. And this book will teach you precisely how. Ready to catapult your practice to new heights? Take a deep breath and dive in....</p>
    </div>
    <svg class="back-mic" role="img" aria-label="Small photo of a vintage chrome microphone on a wooden base" viewBox="0 0 62 185">
      <defs>
        <linearGradient id="micToneBack" x1="0" y1="0" x2="0" y2="1">
          <stop offset="0" stop-color="var(--mic-silver)"/>
          <stop offset="0.8" stop-color="var(--mic-silver)"/>
          <stop offset="1" stop-color="var(--mic-wood)"/>
        </linearGradient>
      </defs>
      <rect width="62" height="185" rx="12" fill="url(#micToneBack)" opacity="0.85"/>
    </svg>
  </section>

  <section class="cover front-cover">
    <h1 class="title">
      <span class="title-small">The Complete</span>
      <span class="title-large">Press Outreach</span>
      <span class="title-large">Guidebook</span>
      <span class="title-small">for Attorneys</span>
    </h1>
    <p class="subtitle">Make Millions using Media and the Internet</p>
    <svg class="front-mic" role="img" aria-label="Photo of a vintage chrome microphone on a round wooden base" viewBox="0 0 112 324">
      <defs>
        <linearGradient id="micToneFront" x1="0" y1="0" x2="0" y2="1">
          <stop offset="0" stop-color="var(--mic-silver)"/>
          <stop offset="0.82" stop-color="var(--mic-silver)"/>
          <stop offset="1" stop-color="var(--mic-wood)"/>
        </linearGradient>
      </defs>
      <rect width="112" height="324" rx="20" fill="url(#micToneFront)" opacity="0.85"/>
    </svg>
    <blockquote class="callout">
      <p>“The definitive PR book.<br>Simple and powerful.”</p>
      <cite>— Hal Brisket</cite>
    </blockquote>
    <div class="credits">
      <p class="credits-label">CO-AUTHORS</p>
      <p class="author">Dale Warbeck, JD</p>
      <p class="author">Mark Tolliver</p>
    </div>
  </section>
</main>
</body>
</html>
```